Marrowby Nature Alliance needs a fundraiser poster

We are having an annual awards night and fundraiser.

On the top of the poster please put "Marrowby Nature Alliance Annual Awards Night and Fundraiser"

Date: March 25, 2023
Time: 6:00pm doors open. Supper at 7:00pm
Location: Quenford Sportsdome Auditorium
Cost: $40 for Adults, $20 for 18 and under

We also would like on the poster, "Live Auctions, Silent auctions, and raffles"
"Serving Elk, Moose, and Wild Boar. Also beef"

```html
<!DOCTYPE html>
<html lang="en">
<head>
<meta charset="utf-8">
<title>Marrowby Nature Alliance Annual Awards Night and Fundraiser</title>
<link rel="stylesheet" href="https://fonts.googleapis.com/css2?family=Montserrat:wght@600;700&family=Oswald:wght@400;500;600&display=swap">
<style>
  :root {
    --stage: #dafd7b;
    --green-deep: #3f9a2e;
    --green-mid: #7cbd3a;
    --green-light: #a9d56c;
    --green-pale: #c9e5a4;
    --quote-faint: #e3efd8;
    --paper: #ffffff;
    --rink: #c9d8cf;
    --crowd: #6f8a52;
  }
  * { margin: 0; padding: 0; box-sizing: border-box; }
  html, body { width: 1200px; height: 960px; overflow: hidden; background: var(--stage); }
  .poster {
    position: absolute; left: 282px; top: 30px;
    width: 636px; height: 900px; overflow: hidden;
    background: linear-gradient(180deg, var(--green-light) 0%, var(--green-mid) 100%);
    box-shadow: 0 18px 40px rgba(60, 100, 20, 0.25);
    font-family: "Oswald", sans-serif;
  }
  .rink-photo {
    position: absolute; right: 0; top: 0; width: 420px; height: 330px;
    background: linear-gradient(90deg, rgba(201,216,207,0) 0%, var(--rink) 55%, #dfe7e2 100%);
  }
  .crowd-photo {
    position: absolute; left: 0; bottom: 0; width: 330px; height: 170px;
    background: linear-gradient(90deg, var(--crowd) 0%, rgba(124,189,58,0.6) 70%, rgba(124,189,58,0) 100%);
  }
  .wave { position: absolute; inset: 0; }
  .brand {
    position: absolute; left: 34px; top: 40px;
    display: flex; align-items: center; gap: 10px;
    font-family: "Montserrat", sans-serif; font-weight: 700;
    color: var(--paper); font-size: 17px; line-height: 1.1;
  }
  .brand-mark { width: 16px; height: 16px; border-radius: 50%; background: var(--paper); }
  .headline { position: absolute; left: 52px; top: 196px; color: var(--green-deep); }
  .headline-org { font-family: "Montserrat", sans-serif; font-weight: 700; font-size: 27px; color: var(--green-mid); }
  .headline-title { font-weight: 600; font-size: 50px; line-height: 1.05; text-transform: uppercase; }
  .headline-sub { font-weight: 600; font-size: 46px; letter-spacing: 12px; line-height: 1.05; text-transform: uppercase; }
  .quote-glyph {
    position: absolute; left: 58px; top: 300px;
    font-family: "Oswald", sans-serif; font-weight: 600; font-size: 380px; line-height: 1;
    color: var(--quote-faint);
  }
  .highlights {
    position: absolute; left: 90px; top: 430px;
    color: var(--green-mid); font-size: 25px; font-weight: 500; line-height: 1.45;
    text-transform: uppercase;
  }
  .details { position: absolute; left: 0; top: 768px; width: 636px; height: 132px; color: var(--paper); }
  .event-date {
    position: absolute; left: 30px; top: 10px; text-align: right;
    font-size: 34px; font-weight: 500; line-height: 1.05;
  }
  .detail-block { position: absolute; padding-left: 12px; border-left: 3px solid var(--paper); }
  .detail-label { font-family: "Montserrat", sans-serif; font-weight: 600; font-size: 15px; }
  .detail-value { font-size: 19px; text-transform: uppercase; line-height: 1.2; }
  .time-block { left: 190px; top: 8px; height: 72px; }
  .venue-block { left: 390px; top: 0; height: 72px; }
  .cost-block { left: 200px; top: 88px; border-left: none; text-align: center; }
</style>
</head>
<body>
  <main class="poster">
    <div class="rink-photo" role="img" aria-label="Photo of a curling rink with ice sheets and target rings"></div>
    <div class="crowd-photo" role="img" aria-label="Photo of guests gathered at a past awards night"></div>

    <svg class="wave" viewBox="0 0 636 900" aria-hidden="true">
      <path d="M0 230 C 180 140, 470 120, 636 270 L636 560 C 520 720, 250 770, 0 775 Z" fill="var(--green-pale)"/>
      <path d="M0 262 C 190 170, 470 160, 610 300 C 650 420, 560 640, 330 720 C 220 750, 100 760, 0 752 Z" fill="var(--paper)"/>
    </svg>

    <div class="brand">
      <span class="brand-mark"></span>
      <span>Marrowby<br>Nature Alliance</span>
    </div>

    <header class="headline">
      <p class="headline-org">Marrowby Nature Alliance</p>
      <h1 class="headline-title">Annual Awards Night</h1>
      <p class="headline-sub">and Fundraiser</p>
    </header>

    <div class="quote-glyph" aria-hidden="true">&ldquo;</div>

    <section class="highlights">
      <p>"Live Auctions, Silent Auctions, and Raffles"</p>
      <p>"Serving Elk, Moose, and Wild Boar. Also Beef"</p>
    </section>

    <section class="details">
      <p class="event-date">March 25<br>2023</p>
      <div class="detail-block time-block">
        <p class="detail-label">6:00pm doors open</p>
        <p class="detail-value">Supper at 7:00pm</p>
      </div>
      <div class="detail-block venue-block">
        <p class="detail-label">Location</p>
        <p class="detail-value">Quenford Sportsdome Auditorium</p>
      </div>
      <div class="detail-block cost-block">
        <p class="detail-label">Cost</p>
        <p class="detail-value">$40 for adults, $20 for 18 and under</p>
      </div>
    </section>
  </main>
</body>
</html>
```